Northlake Imaging Partners
Professional
DMS, RDCS
418 Pellwick Row
Irvine, CA 92606
tvasquell@northlakeimagingpartners.com
www.northlakeimagingpartners.com
Providing high quality ultrasound imaging service in the convenience of the Physician's office.
Increase in quality patient care.
Full body ultrasound 7 days a week
High qulity equipment
Professional staff
Quick turnearound
Your Diagnostic Imaging Specialist
Logo file for NIP stationary

```html
<!DOCTYPE html>
<html lang="en">
<head>
<meta charset="utf-8">
<title>Northlake Imaging Partners – Stationery</title>
<link href="https://fonts.googleapis.com/css2?family=Cinzel:wght@600&family=Open+Sans:wght@400;600&display=swap" rel="stylesheet">
<style>
  :root {
    --bg: #2b2b2d;
    --paper: #ffffff;
    --paper-shade: #e6e4e8;
    --purple: #7d3f8f;
    --purple-light: #a77bb7;
    --grey-line: #c9c6cc;
    --ink: #4a4a4f;
    --ink-soft: #8a8890;
    --envelope-dark: #3c3b3f;
  }
  * { box-sizing: border-box; margin: 0; padding: 0; }
  html, body { width: 1200px; height: 313px; overflow: hidden; background: var(--bg); }
  body { position: relative; font-family: "Open Sans", Arial, sans-serif; color: var(--ink); }

  .piece { position: absolute; background: var(--paper); overflow: hidden; }
  .wave { position: absolute; left: 0; bottom: 0; width: 100%; display: block; }

  .brand { display: flex; align-items: center; gap: 4px; }
  .brand-dot { width: 7px; height: 7px; border-radius: 50%; background: var(--purple); flex: none; }
  .brand-name { font-family: "Cinzel", Georgia, serif; font-weight: 600; color: var(--purple); letter-spacing: .3px; white-space: nowrap; }

  /* logo presentation on dark ground */
  .logo-block { position: absolute; left: 24px; top: 28px; width: 150px; text-align: center; }
  .logo-block .brand { justify-content: center; flex-direction: column; gap: 5px; }
  .logo-block .brand-dot { width: 14px; height: 14px; background: var(--purple-light); }
  .logo-block .brand-name { font-size: 7.4px; color: var(--purple-light); }
  .logo-block .tagline { font-size: 5px; color: var(--ink-soft); margin-top: 3px; }

  /* business card front */
  .card-front { left: 29px; top: 101px; width: 144px; height: 86px; }
  .card-front .brand { position: absolute; left: 0; right: 0; top: 10px; justify-content: center; }
  .card-front .brand-name { font-size: 6px; }
  .card-front .person { position: absolute; left: 0; right: 0; top: 24px; text-align: center; font-size: 4.6px; color: var(--ink-soft); }
  .card-front .contact { position: absolute; left: 8px; bottom: 5px; font-size: 3.6px; color: #fff; line-height: 1.4; }

  /* business card back */
  .card-back { left: 29px; top: 204px; width: 144px; height: 84px; background: var(--purple); color: #fff; padding: 8px 9px; }
  .card-back .intro { font-size: 4.3px; line-height: 1.35; margin-bottom: 4px; }
  .card-back ul { list-style: none; font-size: 4.3px; line-height: 1.55; }
  .card-back li::before { content: "\2713  "; }
  .card-back .spec { position: absolute; right: 9px; bottom: 7px; font-size: 4.3px; font-weight: 600; }

  /* letterheads */
  .letterhead { top: 12px; width: 204px; height: 281px; }
  .letterhead.one { left: 264px; }
  .letterhead.two { left: 492px; }
  .letterhead .brand { position: absolute; left: 0; right: 0; top: 26px; justify-content: center; }
  .letterhead .brand-name { font-size: 6.6px; }
  .letterhead .address { position: absolute; right: 10px; top: 8px; font-size: 3.6px; line-height: 1.4; color: var(--ink-soft); text-align: right; }
  .letterhead .footer { position: absolute; left: 0; right: 0; bottom: 4px; text-align: center; font-size: 3.4px; color: #fff; }

  /* compliment slips */
  .slip { left: 700px; width: 200px; }
  .slip.top { top: 36px; height: 137px; }
  .slip.bottom { top: 180px; height: 103px; }
  .slip .brand { position: absolute; left: 12px; top: 14px; }
  .slip .brand-name { font-size: 5.4px; }
  .slip .address { position: absolute; left: 12px; top: 26px; font-size: 3.6px; line-height: 1.4; color: var(--ink-soft); }
  .slip .footer { position: absolute; left: 12px; bottom: 4px; font-size: 3.4px; color: #fff; }

  /* DL envelopes */
  .envelope { left: 907px; width: 281px; height: 80px; }
  .envelope.dark { top: 22px; background: var(--envelope-dark); }
  .envelope.flap { top: 112px; }
  .envelope.plain { top: 202px; height: 88px; }
  .envelope .flap-shape { position: absolute; left: 0; top: 0; width: 100%; height: 100%; }
  .envelope .brand { position: absolute; left: 0; right: 0; justify-content: center; }
  .envelope.dark .brand { top: 8px; }
  .envelope.dark .brand-name { color: var(--purple-light); }
  .envelope.dark .brand-dot { background: var(--purple-light); }
  .envelope.flap .brand { top: 50px; }
  .envelope.plain .brand { justify-content: flex-start; left: 12px; top: 12px; }
  .envelope .brand-name { font-size: 5.4px; }
  .envelope .address { position: absolute; left: 12px; top: 24px; font-size: 3.4px; line-height: 1.4; color: var(--ink-soft); }
</style>
</head>
<body>

<section class="logo-block" aria-label="Logo">
  <div class="brand"><span class="brand-dot"></span><span class="brand-name">Northlake Imaging Partners</span></div>
  <p class="tagline">Your Diagnostic Imaging Specialist</p>
</section>

<article class="piece card-front" aria-label="Business card front">
  <div class="brand"><span class="brand-dot"></span><span class="brand-name">Northlake Imaging Partners</span></div>
  <p class="person">Professional &middot; DMS, RDCS</p>
  <svg class="wave" viewBox="0 0 144 30" height="30" preserveAspectRatio="none" aria-hidden="true">
    <path d="M0 12 C40 2 90 22 144 6 L144 30 L0 30Z" fill="var(--grey-line)"/>
    <path d="M0 16 C40 6 90 26 144 10 L144 30 L0 30Z" fill="var(--purple)"/>
  </svg>
  <p class="contact">418 Pellwick Row, Irvine, CA 92606<br>tvasquell@northlakeimagingpartners.com</p>
</article>

<article class="piece card-back" aria-label="Business card back">
  <p class="intro">Providing high quality ultrasound imaging service in the convenience of the Physician's office.</p>
  <ul>
    <li>Increase in quality patient care.</li>
    <li>Full body ultrasound 7 days a week</li>
    <li>High quality equipment</li>
    <li>Professional staff</li>
    <li>Quick turnaround</li>
  </ul>
  <p class="spec">www.northlakeimagingpartners.com</p>
</article>

<article class="piece letterhead one" aria-label="Letterhead">
  <p class="address">418 Pellwick Row<br>Irvine, CA 92606<br>tvasquell@northlakeimagingpartners.com</p>
  <div class="brand"><span class="brand-dot"></span><span class="brand-name">Northlake Imaging Partners</span></div>
  <svg class="wave" viewBox="0 0 204 36" height="36" preserveAspectRatio="none" aria-hidden="true">
    <path d="M0 14 C60 0 130 28 204 8 L204 36 L0 36Z" fill="var(--grey-line)"/>
    <path d="M0 19 C60 5 130 32 204 13 L204 36 L0 36Z" fill="var(--purple)"/>
  </svg>
  <p class="footer">www.northlakeimagingpartners.com</p>
</article>

<article class="piece letterhead two" aria-label="Continuation letterhead">
  <div class="brand"><span class="brand-dot"></span><span class="brand-name">Northlake Imaging Partners</span></div>
  <svg class="wave" viewBox="0 0 204 36" height="36" preserveAspectRatio="none" aria-hidden="true">
    <path d="M0 14 C60 0 130 28 204 8 L204 36 L0 36Z" fill="var(--grey-line)"/>
    <path d="M0 19 C60 5 130 32 204 13 L204 36 L0 36Z" fill="var(--purple)"/>
  </svg>
  <p class="footer">www.northlakeimagingpartners.com</p>
</article>

<article class="piece slip top" aria-label="Compliment slip">
  <div class="brand"><span class="brand-dot"></span><span class="brand-name">Northlake Imaging Partners</span></div>
  <p class="address">418 Pellwick Row<br>Irvine, CA 92606</p>
  <svg class="wave" viewBox="0 0 200 28" height="28" preserveAspectRatio="none" aria-hidden="true">
    <path d="M0 10 C60 0 130 24 200 6 L200 28 L0 28Z" fill="var(--grey-line)"/>
    <path d="M0 14 C60 4 130 28 200 10 L200 28 L0 28Z" fill="var(--purple)"/>
  </svg>
  <p class="footer">www.northlakeimagingpartners.com</p>
</article>

<article class="piece slip bottom" aria-label="Note card">
  <div class="brand"><span class="brand-dot"></span><span class="brand-name">Northlake Imaging Partners</span></div>
  <p class="address">418 Pellwick Row<br>Irvine, CA 92606</p>
  <svg class="wave" viewBox="0 0 200 28" height="28" preserveAspectRatio="none" aria-hidden="true">
    <path d="M0 10 C60 0 130 24 200 6 L200 28 L0 28Z" fill="var(--grey-line)"/>
    <path d="M0 14 C60 4 130 28 200 10 L200 28 L0 28Z" fill="var(--purple)"/>
  </svg>
  <p class="footer">www.northlakeimagingpartners.com</p>
</article>

<article class="piece envelope dark" aria-label="Envelope back, dark">
  <svg class="flap-shape" viewBox="0 0 281 80" preserveAspectRatio="none" aria-hidden="true">
    <path d="M0 0 L140.5 46 L281 0Z" fill="#47464b"/>
  </svg>
  <div class="brand"><span class="brand-dot"></span><span class="brand-name">Northlake Imaging Partners</span></div>
</article>

<article class="piece envelope flap" aria-label="Envelope back with purple flap">
  <svg class="flap-shape" viewBox="0 0 281 80" preserveAspectRatio="none" aria-hidden="true">
    <path d="M0 0 L140.5 40 L281 0Z" fill="var(--purple)"/>
    <path d="M0 80 L140.5 70 L281 80" fill="none" stroke="var(--paper-shade)" stroke-width="1"/>
  </svg>
  <div class="brand"><span class="brand-dot"></span><span class="brand-name">Northlake Imaging Partners</span></div>
</article>

<article class="piece envelope plain" aria-label="Envelope front">
  <div class="brand"><span class="brand-dot"></span><span class="brand-name">Northlake Imaging Partners</span></div>
  <p class="address">418 Pellwick Row<br>Irvine, CA 92606</p>
  <svg class="wave" viewBox="0 0 281 18" height="18" preserveAspectRatio="none" aria-hidden="true">
    <path d="M0 8 C90 0 180 16 281 4 L281 18 L0 18Z" fill="var(--purple)"/>
  </svg>
</article>

</body>
</html>
```